Stylish Website Design for Harbour Crate Lagoons

Harbour Crate Lagoons will be building a new website in a Wordpress CMS.
The design will be stylish, clean with strong powerful images that represent their work. Users scrolling pages will have call to actions listed at various intervals that drives traffic through the website journey.
The objective of the website journey is to direct clients to the ‘Instant Quote’. This will take visitors through an 8 Step calculator.
1. Capture Customer Details (Email and Full Name).
2. Pool Size
3. Shell Colour
4. Exterior Colour
5. Decking Option
6. Access Options
7. Selections (choosing the sanitisation and pump)
8. Extras
The instant quote will be visually appealing and engaging. The next button for each step will capture the data and identify the step the customer aborts.
Here is a link to the current calculator OLD QUOTE: https://harbourcratelagoons.example.au/quote
The current design has the following issues that need to be resolved with the new design, please do not replicate the current look and feel. We are seeking a complete redesign of the website.
1. No scrolling to go to the next tap.
2. Improve the image layout
3. Selections and Extras needs to be like an eCommerce site with images, access to descriptions, specifications etc.
4. The steps need to feel like a journey
5. Gathering the customer’s name and email must be captured at the beginning
The aim is to keep the design simple but stylish. The navigation should have a search bar and clearly display the phone number as a link not an image, so it can be clicked on to make a call from a mobile device.
Please note the current website does not have the current logo, only a temporary one. Please use this one, the logo may be redesigned. https://filebay.example.net/external/a1f4c9d2e7b83056f1c2d4e9a7b6c3d8e5f1a2b7c9d0e4f6a8b3c5d7e9f0a1b2
IMAGES: Here are some of the company’s professional images. https://filebay.example.net/external/c7e2a9f1b4d6083e5a1c9f7b2d4e6a8c0f3b5d7e9a1c2f4b6d8e0a3c5f7b9d1e
There must be call to actions as you scroll the page.
• Contact Us Button
• Download Brochure (name may be changed)
o This will capture a customers name and email to send a brochure
• Join Our Team
• Live Chat (Floats bottom right)
• Order Now Button
Site Map
• Home page – via logo
• Design and Build - http://harbourcratelagoons.example.au/learn-more
o Instant Quote
o Packages
There may be 3 packages
o The Process
o Financing
• About Us
o Choosing Us
o Locations
o Careers
• Blogs
o Events
o Legends
• Gallery
• Contact Us
Footer
• Social Media icons
o TikTok
o Instagram
o Facebook
o Youtube
o Twitter
• Privacy Policy (Content on the current site but improve layout)
• Specifications
• Site Map
• Images of Certifications (as shown on the current site)
• Company Contact Details (Address on Phone)
• Marketing News Sign Up
Target Market(s)
Business to Consumer, Renovations
Industry/Entity Type
Construction and Renovations
Number of Pages Required
5+ page
Requirements
Must have
- Read the description but home page design and calculator design.
Nice to have
- Included in the description.

```html
<!DOCTYPE html>
<html lang="en">
<head>
<meta charset="utf-8">
<title>Harbour Crate Lagoons</title>
<link href="https://fonts.googleapis.com/css2?family=Oswald:wght@400;500;600&family=Poppins:ital,wght@0,400;0,500;0,600;1,400&display=swap" rel="stylesheet">
<style>
:root{
  --orange:#f39223;
  --dark:#3b3b3b;
  --ink:#2b2b2b;
  --muted:#6c6c6c;
  --grey:#e9e9e9;
  --white:#ffffff;
}
*{margin:0;padding:0;box-sizing:border-box}
html,body{width:1200px;height:5141px;overflow:hidden;background:var(--white)}
body{position:relative;font-family:"Poppins",sans-serif;color:var(--ink)}
.abs{position:absolute}
.head{font-family:"Oswald",sans-serif;font-weight:500;text-transform:uppercase;color:var(--ink);letter-spacing:-.5px}
.ph{position:absolute}

/* header */
.site-header{position:absolute;left:0;top:0;width:1200px;height:94px;background:var(--white);z-index:3}
.brand{position:absolute;display:flex;align-items:center;gap:10px;font-family:"Poppins",sans-serif;font-weight:600;color:var(--orange);white-space:nowrap}
.brand-dot{width:14px;height:14px;border-radius:50%;background:var(--orange);flex:none}
.nav{position:absolute;top:36px;left:372px;display:flex;gap:26px;font-size:11.5px;font-weight:600;text-transform:uppercase}
.nav-contact{position:absolute;left:794px;top:28px;width:118px;height:38px;background:var(--grey);font-size:11.5px;font-weight:600;display:flex;align-items:center;justify-content:center}
.phone-icon{position:absolute;left:946px;top:28px;width:38px;height:38px;background:var(--orange);display:flex;align-items:center;justify-content:center}
.phone-text{position:absolute;left:994px;top:28px;font-size:12px;line-height:18px}
.phone-text b{font-weight:600;font-size:11px}

/* hero */
.hero{position:absolute;left:0;top:94px;width:1200px;height:704px;background:linear-gradient(180deg,#b5763a 0%,#7a6a55 30%,#3a4d7a 60%,#2330a8 85%,#4150b8 100%)}
.hero-title{position:absolute;top:330px;left:0;width:1200px;text-align:center;font-family:"Oswald",sans-serif;font-weight:600;font-size:60px;line-height:64px;color:var(--white);text-transform:uppercase;letter-spacing:-1.5px}
.hero-sub{position:absolute;top:472px;left:0;width:1200px;text-align:center;font-family:"Oswald",sans-serif;font-size:15px;color:var(--white);text-transform:uppercase;letter-spacing:-.3px}
.btn-white{position:absolute;left:526px;top:516px;width:148px;height:40px;background:var(--white);font-size:12px;font-weight:600;display:flex;align-items:center;justify-content:center}

/* sustainable */
.sec-title{position:absolute;left:0;width:1200px;text-align:center;font-size:48px}
.feature-band{position:absolute;left:598px;top:1196px;width:602px;height:340px;background:var(--orange)}
.card{position:absolute;background:var(--white);box-shadow:0 10px 30px rgba(0,0,0,.08)}
.card-title{font-family:"Oswald",sans-serif;font-weight:500;font-size:17px;text-transform:uppercase}
.card-body{font-size:12.5px;line-height:20px;color:var(--muted)}
.explore{font-size:13px;color:var(--muted);display:flex;align-items:center;gap:6px}
.explore span{border-bottom:1px solid var(--muted)}

/* about */
.about-label{position:absolute;left:646px;top:1712px;font-family:"Oswald",sans-serif;font-size:17px;font-weight:500;padding-bottom:6px;border-bottom:1px solid var(--ink);width:176px}
.about-text{position:absolute;left:646px;top:1826px;width:440px;font-size:14.5px;line-height:24px;color:var(--muted)}
.btn-grey{position:absolute;background:var(--grey);font-size:12px;font-weight:600;display:flex;align-items:center;justify-content:center}

/* quote */
.size-card{position:absolute;top:2524px;width:146px;height:154px;background:var(--white);display:flex;align-items:center;justify-content:center}
.size-circle{width:100px;height:100px;border-radius:50%;background:var(--grey);display:flex;flex-direction:column;align-items:center;justify-content:center}
.size-circle b{font-family:"Oswald",sans-serif;font-size:26px;font-weight:600;line-height:28px}
.size-circle span{font-size:10px}

/* testimonial */
.avatar{position:absolute;border-radius:50%;background:linear-gradient(135deg,#d6d0c8,#9a948c);border:3px solid var(--white);box-shadow:0 4px 12px rgba(0,0,0,.15)}

/* blog */
.blog-meta{font-size:11px;color:var(--muted)}
.blog-title{font-family:"Oswald",sans-serif;font-weight:500;font-size:18px;line-height:23px;text-transform:uppercase}

/* footer */
.foot-col{position:absolute;top:4806px;color:var(--white)}
.foot-col h4{font-family:"Oswald",sans-serif;font-weight:400;font-size:17px;text-transform:uppercase;margin-bottom:14px}
.foot-col li{list-style:none;font-size:12px;line-height:28px}
.social{position:absolute;top:4958px;width:28px;height:28px;border-radius:50%;border:1px solid #8a8a8a}
</style>
</head>
<body>

<header class="site-header">
  <div class="brand" style="left:94px;top:36px;font-size:17px"><span class="brand-dot"></span>Harbour Crate Lagoons</div>
  <nav class="nav"><span>Home</span><span>About Us</span><span>Instant Quote</span><span>Blogs</span><span>Gallery</span></nav>
  <div class="nav-contact">CONTACT US</div>
  <div class="phone-icon"><svg width="16" height="16" viewBox="0 0 24 24"><path fill="#fff" d="M6.6 10.8a15 15 0 0 0 6.6 6.6l2.2-2.2c.3-.3.7-.4 1-.2 1.1.4 2.3.6 3.6.6.6 0 1 .4 1 1V20c0 .6-.4 1-1 1A17 17 0 0 1 3 4c0-.6.4-1 1-1h3.5c.6 0 1 .4 1 1 0 1.3.2 2.5.6 3.6.1.3 0 .7-.2 1z"/></svg></div>
  <div class="phone-text"><b>PHONE*</b><br>+08 555 010 2040</div>
</header>

<section class="hero" role="img" aria-label="Photo of a long glass-fenced container pool at sunset overlooking a town"></section>
<h1 class="hero-title">Why choose a Harbour Crate<br>Lagoon?</h1>
<p class="hero-sub">Using the latest in technologies we are able to create a light weight product that can easily</p>
<div class="btn-white">ORDER NOW</div>

<!-- sustainable -->
<h2 class="head sec-title" style="top:890px">Sustainable</h2>
<div class="feature-band"></div>
<svg class="abs" style="left:660px;top:1436px" width="480" height="54" viewBox="0 0 480 54">
  <circle cx="36" cy="26" r="25" fill="none" stroke="#fff" stroke-width="2"/>
  <path d="M44 26H28m6-6-6 6 6 6" fill="none" stroke="#fff" stroke-width="2"/>
  <line x1="82" y1="26" x2="394" y2="26" stroke="#fff" stroke-width="2"/>
  <circle cx="440" cy="26" r="25" fill="none" stroke="#fff" stroke-width="2"/>
  <path d="M432 26h16m-6-6 6 6-6 6" fill="none" stroke="#fff" stroke-width="2"/>
</svg>

<article class="card" style="left:88px;top:980px;width:322px;height:406px">
  <div class="ph" style="left:0;top:0;width:322px;height:216px;background:linear-gradient(180deg,#9fb7cc,#5f7250 70%,#3d4a33)" role="img" aria-label="Photo of a raised container pool on a steel frame among trees"></div>
  <div class="abs" style="left:30px;top:244px;width:270px">
    <div class="card-title">Our Smart</div>
    <p class="card-body" style="margin-top:8px">The factory assembled filtration system is housed within the container, just PLUG &gt; FILL &gt; PLAY...</p>
    <div class="explore" style="margin-top:12px"><span>Explore</span>→</div>
  </div>
</article>
<article class="card" style="left:438px;top:980px;width:322px;height:406px">
  <div class="ph" style="left:0;top:0;width:322px;height:216px;background:linear-gradient(180deg,#7ea9cf,#6d8a62 55%,#8a7a66)" role="img" aria-label="Photo of a pool deck with child-safety fencing under a pergola"></div>
  <div class="abs" style="left:26px;top:244px;width:270px">
    <div class="card-title">Our Safe</div>
    <p class="card-body" style="margin-top:8px">Through the child-safety door wide wooden stairs leads up to a landing allowing easy access into...</p>
    <div class="explore" style="margin-top:12px"><span>Explore</span>→</div>
  </div>
</article>
<article class="card" style="left:788px;top:980px;width:322px;height:406px">
  <div class="ph" style="left:0;top:0;width:322px;height:216px;background:linear-gradient(180deg,#6d7aa0,#c48a56 45%,#7a5a3c)" role="img" aria-label="Photo of a deck lounge with a hanging chair at sunset"></div>
  <div class="abs" style="left:26px;top:244px;width:270px">
    <div class="card-title">Our Play</div>
    <p class="card-body" style="margin-top:8px">With a smooth and nonporous surface, algae have nothing to attach to, maing cleaning your pool 90%...</p>
    <div class="explore" style="margin-top:12px"><span>Explore</span>→</div>
  </div>
</article>

<!-- about -->
<div class="ph" style="left:88px;top:1772px;width:350px;height:512px;background:linear-gradient(160deg,#5f6e3a,#3d5a36 40%,#3fa6c8 60%,#6fc1dc)" role="img" aria-label="Photo looking down a pool edge with glass fence over a forest"></div>
<div class="ph" style="left:272px;top:1614px;width:276px;height:322px;background:var(--white);box-shadow:0 10px 30px rgba(0,0,0,.15)"></div>
<div class="ph" style="left:284px;top:1626px;width:252px;height:298px;background:linear-gradient(180deg,#8fb3d8,#6f8aa0 40%,#3f88d0 70%,#5ea6e0)" role="img" aria-label="Photo of a narrow infinity pool overlooking hills"></div>
<div class="about-label">ABOUT US</div>
<h2 class="head abs" style="left:646px;top:1744px;font-size:50px">Any Home &amp; Any Site</h2>
<p class="about-text">Previously pools were limited by the landscape of the property and requirement to excavate. With the Harbour Crate Lagoon design you can place a pool where you once couldn't. A flexible and intuitive design with technical structural support, means your new pool installation is only limited by your imagination!<br><br>Shipping Country wide!</p>
<div class="btn-grey" style="left:646px;top:2058px;width:164px;height:38px">BUILD YOUR POOL</div>

<!-- instant quote -->
<svg class="abs" style="left:0;top:2240px" width="1200" height="720" viewBox="0 0 1200 720">
  <defs><linearGradient id="qbg" x1="0" y1="0" x2="1" y2="0"><stop offset="0" stop-color="#3a3a3a"/><stop offset=".5" stop-color="#4a4a4a"/><stop offset="1" stop-color="#3a3a3a"/></linearGradient></defs>
  <polygon points="0,0 1200,0 1200,290 0,660" fill="url(#qbg)"/>
  <polygon points="0,660 1200,290 1200,312 0,712" fill="#f39223"/>
</svg>
<div class="abs" style="left:380px;top:2340px;font-family:'Oswald',sans-serif;font-weight:600;font-size:150px;color:rgba(255,255,255,.08);line-height:150px">01</div>
<h2 class="head abs" style="left:88px;top:2398px;font-size:44px;color:var(--white)">Instant Quote</h2>
<div class="abs" style="left:88px;top:2488px;font-family:'Oswald',sans-serif;font-size:17px;color:var(--white)">SELECT A POOL SIZE*</div>
<div class="size-card" style="left:88px"><div class="size-circle"><b>6M</b><span>6M X 2.4M</span></div></div>
<div class="size-card" style="left:248px"><div class="size-circle"><b>12M</b><span>12M X 2.4M</span></div></div>
<svg class="abs" style="left:90px;top:2710px" width="120" height="54" viewBox="0 0 120 54">
  <circle cx="28" cy="26" r="24" fill="none" stroke="#fff" stroke-width="2"/><path d="M36 26H20m6-6-6 6 6 6" fill="none" stroke="#fff" stroke-width="2"/>
  <circle cx="90" cy="26" r="24" fill="none" stroke="#fff" stroke-width="2"/><path d="M82 26h16m-6-6 6 6-6 6" fill="none" stroke="#fff" stroke-width="2"/>
</svg>
<div class="ph" style="left:696px;top:2344px;width:414px;height:548px;background:var(--orange);box-shadow:0 14px 30px rgba(0,0,0,.2)"></div>
<div class="ph" style="left:712px;top:2360px;width:382px;height:516px;background:var(--white)"></div>
<div class="ph" style="left:770px;top:2396px;width:270px;height:250px;background:linear-gradient(135deg,#3a3a3a,#1f6fe0 50%,#2a2a2a)" role="img" aria-label="Illustration of a container pool in perspective"></div>
<div class="ph" style="left:748px;top:2684px;width:312px;height:124px;background:linear-gradient(90deg,#555,#1f7ae8 15%,#2a8af0 85%,#555)" role="img" aria-label="Illustration of a container pool seen from above"></div>
<svg class="abs" style="left:666px;top:2856px" width="70" height="90" viewBox="0 0 70 90">
  <g fill="none" stroke="#333" stroke-width="2"><circle cx="8" cy="8" r="3"/><circle cx="8" cy="30" r="3"/><circle cx="8" cy="52" r="3"/><circle cx="8" cy="74" r="3"/><circle cx="34" cy="74" r="3"/><circle cx="60" cy="74" r="3"/><circle cx="60" cy="52" r="3"/></g>
</svg>
<div class="ph" style="left:203px;top:2930px;width:3px;height:130px;background:var(--orange)"></div>

<!-- gallery -->
<h2 class="head abs" style="left:88px;top:3064px;font-size:48px">Our Gallery</h2>
<div class="ph" style="left:88px;top:3146px;width:246px;height:266px;background:linear-gradient(180deg,#c8ccd0,#2f6fd0 60%,#4a4a4a)" role="img" aria-label="Photo of a pool with glass fence"></div>
<div class="ph" style="left:346px;top:3146px;width:246px;height:266px;background:linear-gradient(180deg,#4f78b8,#d88a4a 45%,#2a40c0 75%,#1e2a80)" role="img" aria-label="Photo of a pool at sunset"></div>
<div class="ph" style="left:604px;top:3146px;width:246px;height:266px;background:linear-gradient(180deg,#8fb0d0,#557a48 40%,#4f5a6a)" role="img" aria-label="Photo of a raised container pool beside a house"></div>
<div class="ph" style="left:862px;top:3146px;width:246px;height:266px;background:linear-gradient(180deg,#7c8a74,#7cc0e0 40%,#a8d8ec 70%,#6a6a6a)" role="img" aria-label="Photo of a pool seen from above"></div>
<div class="ph" style="left:1118px;top:3146px;width:82px;height:266px;background:linear-gradient(180deg,#6f9a5a,#4a5a6a)" role="img" aria-label="Photo of a container pool among trees"></div>

<!-- testimonial -->
<div class="avatar" style="left:410px;top:3556px;width:46px;height:46px" role="img" aria-label="Customer portrait"></div>
<div class="avatar" style="left:482px;top:3556px;width:46px;height:46px" role="img" aria-label="Customer portrait"></div>
<div class="avatar" style="left:548px;top:3530px;width:88px;height:88px;border-width:4px" role="img" aria-label="Customer portrait"></div>
<div class="avatar" style="left:660px;top:3556px;width:46px;height:46px" role="img" aria-label="Customer portrait"></div>
<div class="avatar" style="left:732px;top:3556px;width:46px;height:46px" role="img" aria-label="Customer portrait"></div>
<svg class="abs" style="left:550px;top:3626px" width="100" height="18" viewBox="0 0 100 18">
  <g fill="#f39223"><path id="st" d="M9 1l2.4 5 5.4.7-4 3.8 1 5.4L9 13.3 4.2 15.9l1-5.4-4-3.8 5.4-.7z"/><use href="#st" x="20"/><use href="#st" x="40"/><use href="#st" x="60"/></g>
  <use href="#st" x="80" fill="#ddd"/>
</svg>
<div class="abs" style="left:222px;top:3640px;font-family:'Oswald',sans-serif;font-weight:600;font-size:90px;color:var(--orange);line-height:90px">“</div>
<div class="abs" style="left:752px;top:3700px;font-family:'Oswald',sans-serif;font-weight:600;font-size:90px;color:var(--orange);line-height:90px">”</div>
<p class="abs" style="left:270px;top:3672px;width:660px;text-align:center;font-style:italic;font-size:15.5px;line-height:26px;color:var(--muted)">Aenean vulputate eleifend tellus aenean leo ligula, porttitor eu consequat vitae eleifend ac enim aliquam lorem ante.</p>
<div class="abs" style="left:0;top:3744px;width:1200px;text-align:center;font-size:12px;font-weight:500">MARLO VENN</div>
<svg class="abs" style="left:1100px;top:3620px" width="16" height="70" viewBox="0 0 16 70">
  <circle cx="8" cy="8" r="5" fill="none" stroke="#333" stroke-width="2"/><circle cx="8" cy="28" r="3" fill="none" stroke="#333" stroke-width="1.5"/><circle cx="8" cy="46" r="3" fill="none" stroke="#333" stroke-width="1.5"/>
</svg>

<!-- blog -->
<h2 class="head sec-title" style="top:3866px">Latest Blog</h2>
<article class="card" style="left:162px;top:3948px;width:280px;height:402px">
  <div class="ph" style="left:0;top:0;width:280px;height:218px;background:linear-gradient(180deg,#e0a050,#b0704a 40%,#4a5a3a)" role="img" aria-label="Photo of a pool deck at sunset"></div>
  <div class="abs" style="left:26px;top:256px;width:230px"><div class="blog-meta">byRavi &nbsp;•&nbsp; January 2021</div><div class="blog-title" style="margin-top:6px">Stay up to date with our latest news.</div><p class="card-body" style="font-size:12px;margin-top:10px">Aenean sollicitudin bibendum is a auctor, nisi elit consequat...</p></div>
</article>
<article class="card" style="left:460px;top:3948px;width:280px;height:402px">
  <div class="ph" style="left:0;top:0;width:280px;height:218px;background:linear-gradient(180deg,#6a8a5a,#9aa0a8 40%,#2a70d8 75%,#3a80e0)" role="img" aria-label="Photo of a pool in front of a modern house"></div>
  <div class="abs" style="left:26px;top:256px;width:230px"><div class="blog-meta">byRavi &nbsp;•&nbsp; January 2021</div><div class="blog-title" style="margin-top:6px">Stay up to date with our latest news.</div><p class="card-body" style="font-size:12px;margin-top:10px">Aenean sollicitudin bibendum is a auctor, nisi elit consequat...</p></div>
</article>
<article class="card" style="left:758px;top:3948px;width:280px;height:402px">
  <div class="ph" style="left:0;top:0;width:280px;height:218px;background:linear-gradient(180deg,#a0b8d0,#8a7050 45%,#5aa8d8 75%,#7a6a4a)" role="img" aria-label="Photo of a raised pool beside a timber house"></div>
  <div class="abs" style="left:26px;top:256px;width:230px"><div class="blog-meta">byRavi &nbsp;•&nbsp; January 2021</div><div class="blog-title" style="margin-top:6px">Stay up to date with our latest news.</div><p class="card-body" style="font-size:12px;margin-top:10px">Aenean sollicitudin bibendum is a auctor, nisi elit consequat...</p></div>
</article>

<!-- footer -->
<svg class="abs" style="left:0;top:4350px" width="1200" height="791" viewBox="0 0 1200 791">
  <polygon points="0,10 1200,140 1200,791 0,791" fill="#3b3b3b"/>
  <polygon points="520,66 1200,90 1200,214" fill="#f39223"/>
  <polygon points="560,72 1200,140 1200,224" fill="#3b3b3b"/>
</svg>
<h2 class="head sec-title" style="top:4594px;color:var(--white);font-size:46px">Newsletter</h2>
<div class="ph" style="left:340px;top:4680px;width:402px;height:46px;background:var(--white);display:flex;align-items:center;padding-left:20px;font-size:12.5px;color:var(--muted);gap:8px">
  <svg width="14" height="10" viewBox="0 0 14 10"><rect x=".5" y=".5" width="13" height="9" fill="none" stroke="#888"/><path d="M.5.5 7 5.5 13.5.5" fill="none" stroke="#888"/></svg>Enter your email address</div>
<div class="ph" style="left:742px;top:4680px;width:118px;height:46px;background:var(--orange);color:var(--white);font-size:12px;font-weight:600;display:flex;align-items:center;justify-content:center">SUBSCRIBE</div>

<div class="brand" style="left:92px;top:4850px;font-size:15px"><span class="brand-dot"></span>Harbour Crate Lagoons</div>
<div class="social" style="left:92px"></div><div class="social" style="left:134px"></div><div class="social" style="left:176px"></div><div class="social" style="left:220px"></div><div class="social" style="left:262px"></div>

<div class="foot-col" style="left:368px"><h4>Quick Links</h4><ul><li>› About Us</li><li>› Instant Quote</li><li>› Blogs</li><li>› Gallery</li><li>› Contact Us</li></ul></div>
<div class="foot-col" style="left:548px"><h4>Company</h4><ul><li>› Privacy Policy</li><li>› Specifications</li><li>› Site Map</li></ul></div>
<div class="foot-col" style="left:734px"><h4>Information</h4><ul><li>› Privacy Policy</li><li>› Return Policy</li><li>› Terms &amp; Condition</li><li>› Contact us</li><li>› FAQ's</li></ul></div>
<div class="foot-col" style="left:916px;width:210px">
  <h4>Contact Info</h4>
  <div style="font-size:12.5px;line-height:22px;padding-left:24px;position:relative"><span style="position:absolute;left:0;top:4px;width:12px;height:9px;background:var(--orange)"></span>Email:<br>www.example.com</div>
  <div style="font-size:12.5px;line-height:22px;padding-left:24px;position:relative;margin-top:18px"><span style="position:absolute;left:0;top:5px;width:10px;height:10px;border-radius:50%;background:var(--orange)"></span>Phone:<br>(+08) 555-010-20</div>
  <div style="font-size:12.5px;line-height:22px;padding-left:24px;position:relative;margin-top:14px"><svg style="position:absolute;left:0;top:4px" width="10" height="14" viewBox="0 0 10 14"><path d="M5 0a5 5 0 0 0-5 5c0 4 5 9 5 9s5-5 5-9a5 5 0 0 0-5-5zm0 7a2 2 0 1 1 0-4 2 2 0 0 1 0 4z" fill="#f39223"/></svg>Location:<br>Some address line goes<br>here city name</div>
</div>

<div class="abs" style="left:0;top:5102px;width:1200px;text-align:center;font-family:'Oswald',sans-serif;font-size:12px;color:var(--white)">© 2021, HARBOUR CRATE LAGOONS ALL RIGHTS RESERVED</div>
<div class="ph" style="left:1134px;top:5082px;width:48px;height:48px;border-radius:50%;background:var(--orange);display:flex;align-items:center;justify-content:center">
  <svg width="22" height="22" viewBox="0 0 22 22"><path d="M11 2a8 8 0 0 0-7 12l-1.5 5 5-1.5A8 8 0 1 0 11 2z" fill="#fff"/></svg>
</div>

</body>
</html>
```